Book Cover - For Best Selling Diet

Hi
Book cover required for a diet book being marketed to become a best seller
For best quality, image will be 2820 pixels on the shortest side and 4500 pixels on the longest side .
The book name : Bright Morning Plan
By Corinna Plett
( will add in the extra text once we see design - top and bottom subtitle )
I do not want a photo of a person on the book.
PLEASE SEE " THE 9 STEP FRAME" by Ned Galbury as an example of solid style and I also love Quiet Ledger for the font.
Branding Colours:
#F26432
#A4195C
#A7D8CC
Font that runs through our brand is : helvetica neue
This is for a book that will be marketed for #1 bestseller - So please only quality
designs that are designed in a unique style.
Thanks
Target Market(s)
Busy Working Mums, Affluent, 30+ .
Look and feel

```html
<!DOCTYPE html>
<html lang="en">
<head>
<meta charset="utf-8">
<title>Bright Morning Plan – Book Cover</title>
<link rel="stylesheet" href="https://fonts.googleapis.com/css2?family=Inter:wght@100;200&display=swap">
<style>
  :root {
    --brand-orange: #F26432;
    --brand-coral: #E0423E;
    --brand-magenta: #A4195C;
    --type-white: #FFFFFF;
    --page-bg: #FFFFFF;
  }
  * { margin: 0; padding: 0; box-sizing: border-box; }
  html, body {
    width: 930px;
    height: 1200px;
    overflow: hidden;
    background: var(--page-bg);
  }
  .stage {
    position: relative;
    width: 930px;
    height: 1200px;
  }
  .book-cover {
    position: absolute;
    left: 115px;
    top: 40px;
    width: 700px;
    height: 1120px;
    overflow: hidden;
    background: linear-gradient(180deg, var(--brand-orange) 0%, var(--brand-coral) 40%, var(--brand-magenta) 100%);
    color: var(--type-white);
    font-family: "Inter", "Helvetica Neue", Helvetica, Arial, sans-serif;
    font-weight: 100;
    text-align: center;
  }
  .cover-title {
    font-size: inherit;
    font-weight: 100;
  }
  .cover-line {
    position: absolute;
    left: 0;
    right: 0;
    display: block;
    line-height: 1;
    white-space: nowrap;
    font-weight: 100;
  }
  .title-top {
    top: 296px;
    font-size: 60px;
    letter-spacing: 0;
  }
  .title-main {
    top: 351px;
    font-size: 280px;
    letter-spacing: -4px;
  }
  .byline-label {
    top: 648px;
    font-size: 70px;
    font-weight: 200;
  }
  .author-name {
    top: 722px;
    font-size: 78px;
    font-weight: 200;
  }
</style>
</head>
<body>
  <main class="stage">
    <section class="book-cover" aria-label="Book cover">
      <h1 class="cover-title">
        <span class="cover-line title-top">BRIGHT MORNING</span>
        <span class="cover-line title-main">Plan</span>
      </h1>
      <p class="cover-line byline-label">BY</p>
      <p class="cover-line author-name">Corinna Plett</p>
    </section>
  </main>
</body>
</html>
```